***Dappled Fern Lash Studio is in need of a web site makeover***

I need a makeover for my existing web site. www.dappled-fern.com

Please help!!!! Thanks 😁

Dappled Fern Lash Studio is an eyelash extension salon. In addition, we also provide skincare services (facials, waxing, etc). Our web site needs to appear professional and intuitive. In addition, allowing for ease of online booking is of utmost importance.

The client web site experience:
- esthetically pleasing and makes sense
- clearly recognize brand (Dappled Fern)
- easy to follow web pages
- easy to book appointments online
- easy to sign up for email updates
- easily locate services menu and pricing

Target Market(s)

Dappled Fern Lash Studio offers eyelash extension services, as well as various skincare services (I.e. facials, waxing, etc.)

Industry/Entity Type

Beauty Salon

Number of Pages Required

5+ page

Font styles to use
Sans Serif
Script

Colors
000000
fee3d5
eaeaea
ffffff

Requirements
Must have
• - Home page with static contact information
• - Services page (menu of services and pricing)
• - Photo gallery page
• - Contact page
• - Q&A page
Nice to have
• Professional, classy, intuitive and simple for clients to be able to book online.

```html
<!DOCTYPE html>
<html lang="en">
<head>
<meta charset="utf-8">
<title>Dappled Fern Lash Studio</title>
<link href="https://fonts.googleapis.com/css2?family=Josefin+Sans:wght@400;600;700&family=Open+Sans:wght@400;600&family=Lora:ital@1&display=swap" rel="stylesheet">
<style>
:root{
  --black:#000000;
  --blush:#fee3d5;
  --grey:#eaeaea;
  --white:#ffffff;
  --ink:#1a1a1a;
  --muted:#6b6b6b;
}
*{box-sizing:border-box;margin:0;padding:0}
html,body{width:1200px;height:2200px;overflow:hidden}
body{position:relative;background:var(--white);font-family:"Open Sans",Arial,sans-serif;color:var(--ink)}
.display{font-family:"Josefin Sans",Arial,sans-serif}
.script{font-family:"Lora",Georgia,serif;font-style:italic}

/* hero */
.hero{position:absolute;left:0;top:0;width:1200px;height:600px;
  background:linear-gradient(100deg,#f6ece6 0%,#efdfd5 30%,#c9a894 55%,#8a6a5c 75%,#e8dcd6 100%)}
.site-nav{position:absolute;left:100px;top:40px;width:1000px;height:64px;background:var(--white);
  display:flex;align-items:center;padding:0 20px;box-shadow:0 2px 8px rgba(0,0,0,.12)}
.brand{font-family:"Josefin Sans",Arial,sans-serif;font-weight:700;font-size:26px;color:var(--black);margin-right:auto}
.nav-links{display:flex;gap:6px;list-style:none;margin-right:26px}
.nav-links li{font-size:13px;padding:8px 14px;color:var(--ink)}
.nav-links li.active{background:var(--black);color:var(--white)}
.book-btn{background:var(--black);color:var(--white);font-size:13px;padding:10px 18px;display:flex;align-items:center;gap:8px}
.hero-copy{position:absolute;left:100px;top:270px}
.hero-copy h1{font-family:"Josefin Sans",Arial,sans-serif;font-weight:700;font-size:58px;line-height:1.05;color:var(--black)}
.hero-copy p{font-size:26px;margin-top:14px;color:var(--ink)}
.btn-dark{display:inline-block;background:var(--black);color:var(--white);font-size:14px;padding:12px 22px;margin-top:24px}
.dots{display:flex;gap:8px;margin-top:18px}
.dots span{width:9px;height:9px;border-radius:50%;background:var(--white)}
.dots span.on{background:var(--black)}

.booking{position:absolute;left:820px;top:188px;width:270px;height:350px;background:var(--white);box-shadow:0 4px 14px rgba(0,0,0,.18)}
.booking h2{background:var(--black);color:var(--white);font-family:"Josefin Sans",Arial,sans-serif;font-size:20px;font-weight:600;padding:16px 18px}
.booking form{padding:16px 18px}
.field{height:38px;border:1px solid #cfcfcf;font-size:13px;color:var(--muted);padding:10px 10px;margin-bottom:12px;display:flex;justify-content:space-between}
.submit{display:inline-block;background:var(--black);color:var(--white);font-size:14px;padding:10px 20px;margin-top:4px}

/* services */
.section-title{font-family:"Josefin Sans",Arial,sans-serif;font-weight:700;font-size:40px;color:var(--black)}
.section-sub{font-size:15px;color:var(--muted);margin-top:10px}
.section-sub b{color:var(--black)}
.services{position:absolute;left:0;top:600px;width:1200px;height:520px;text-align:center;padding-top:52px}
.cards{position:absolute;left:100px;top:140px;width:1000px;display:flex;justify-content:space-between}
.card{position:relative;width:316px;height:330px}
.card .photo{position:absolute;inset:0}
.card .label{position:absolute;left:0;right:0;bottom:0;height:62px;background:rgba(0,0,0,.88);color:var(--white);
  display:flex;align-items:center;justify-content:space-between;padding:0 18px}
.card .label strong{font-family:"Josefin Sans",Arial,sans-serif;font-weight:600;font-size:28px}
.card .label span{font-size:14px}

/* sign up */
.signup{position:absolute;left:0;top:1120px;width:1200px;height:300px;background:linear-gradient(90deg,#f4e0d6,var(--blush))}
.signup .photo{position:absolute;left:0;top:0;width:780px;height:300px;
  background:linear-gradient(90deg,#e9d3c7,#d8b8a8 30%,#e7cfc3 50%,#d5b3a2 70%,#f1dcd1)}
.signup-form{position:absolute;left:800px;top:50px;width:300px}
.signup-form h2{font-family:"Josefin Sans",Arial,sans-serif;font-weight:700;font-size:40px;color:var(--black)}
.signup-form p{font-size:14px;color:var(--muted);margin:8px 0 24px}
.signup-form .field{background:var(--white);width:300px;height:46px;padding:14px}

/* gallery */
.gallery{position:absolute;left:100px;top:1420px;width:1000px;height:500px;padding-top:40px}
.gallery-row{display:flex;justify-content:space-between;margin-top:34px}
.gallery-row .photo{width:316px;height:320px}

/* footer */
.site-footer{position:absolute;left:0;top:1920px;width:1200px;height:280px;background:var(--blush)}
.footer-cols{position:absolute;left:100px;top:40px;width:1000px;display:flex;justify-content:space-between}
.footer-col{width:290px}
.footer-col h3{font-family:"Josefin Sans",Arial,sans-serif;font-weight:700;font-size:30px;color:var(--black);margin-bottom:14px}
.footer-col p{font-size:13px;line-height:1.6;color:#4a4a4a}
.social{display:flex;gap:10px;margin-top:18px}
.social span{width:32px;height:32px;border:1px solid var(--black);background:var(--white)}
.footer-bar{position:absolute;left:100px;top:238px;width:1000px;display:flex;justify-content:space-between;font-size:12px;color:#4a4a4a;border-top:1px solid #e3c7b8;padding-top:12px}
.footer-bar ul{display:flex;gap:10px;list-style:none}
</style>
</head>
<body>

<header class="hero" role="img" aria-label="Close-up photo of a woman with long eyelash extensions">
  <nav class="site-nav">
    <div class="brand">Dappled Fern</div>
    <ul class="nav-links">
      <li class="active">Home</li><li>About us</li><li>Services</li><li>Pricing</li><li>Gallery</li><li>Contact</li>
    </ul>
    <div class="book-btn">
      <svg width="14" height="14" viewBox="0 0 14 14"><rect x="1" y="2" width="12" height="11" fill="none" stroke="#fff" stroke-width="1.5"/><line x1="1" y1="5.5" x2="13" y2="5.5" stroke="#fff" stroke-width="1.5"/></svg>
      Book Appointment
    </div>
  </nav>
  <div class="hero-copy">
    <h1>Eyelashes<br>Improvement</h1>
    <p class="script">blues, browns, blacks and greys</p>
    <span class="btn-dark">See Offers</span>
    <div class="dots"><span class="on"></span><span></span><span></span></div>
  </div>
</header>

<aside class="booking">
  <h2>Book Now</h2>
  <form>
    <div class="field">Name</div>
    <div class="field">Email</div>
    <div class="field">Service <svg width="10" height="10" viewBox="0 0 10 10"><path d="M1 3l4 4 4-4" fill="none" stroke="#666" stroke-width="1.5"/></svg></div>
    <div class="field">Date <svg width="10" height="10" viewBox="0 0 10 10"><path d="M1 3l4 4 4-4" fill="none" stroke="#666" stroke-width="1.5"/></svg></div>
    <span class="submit">Submit</span>
  </form>
</aside>

<section class="services">
  <h2 class="section-title">Services we offer</h2>
  <p class="section-sub script">We take care of your beauty and we can make you happy like never before. Need more? <b>Contact us!</b></p>
  <div class="cards">
    <div class="card">
      <div class="photo" role="img" aria-label="Photo of a woman relaxing during a facial treatment" style="background:linear-gradient(135deg,#e8c9b3,#c99a7d 60%,#f1dccd)"></div>
      <div class="label"><strong>Facials</strong><span>1 hour $ 30</span></div>
    </div>
    <div class="card">
      <div class="photo" role="img" aria-label="Photo of a waxing treatment on skin" style="background:linear-gradient(135deg,#f3ddd0,#d9a98f 55%,#f6e6dc)"></div>
      <div class="label"><strong>Waxing</strong><span>1 hour $ 30</span></div>
    </div>
    <div class="card">
      <div class="photo" role="img" aria-label="Photo of an eye with pink and purple eye shadow" style="background:linear-gradient(135deg,#d88bc0,#8a3a7a 50%,#2a1a22)"></div>
      <div class="label"><strong>Skincare</strong><span>1 hour $ 30</span></div>
    </div>
  </div>
</section>

<section class="signup">
  <div class="photo" role="img" aria-label="Photo of a woman's eyes with natural lashes"></div>
  <div class="signup-form">
    <h2>Sign up</h2>
    <p class="script">Sign up get exclusive offers to your email!</p>
    <div class="field">Enter Your Email</div>
    <span class="submit">Submit</span>
  </div>
</section>

<section class="gallery">
  <h2 class="section-title">Gallery</h2>
  <p class="section-sub script">We take care of your beauty and we can make you happy like never before. Need more? <b>Contact us!</b></p>
  <div class="gallery-row">
    <div class="photo" role="img" aria-label="Photo of eye makeup being applied" style="background:linear-gradient(135deg,#e9cdbd,#b98671 50%,#5c3f35)"></div>
    <div class="photo" role="img" aria-label="Photo of a makeup artist applying lash makeup" style="background:linear-gradient(135deg,#f5ece6,#e3c4a6 50%,#f0e2d8)"></div>
    <div class="photo" role="img" aria-label="Photo of a blonde woman getting her makeup done" style="background:linear-gradient(135deg,#f2ebe6,#dcc0a2 50%,#c7a889)"></div>
  </div>
</section>

<footer class="site-footer">
  <div class="footer-cols">
    <div class="footer-col">
      <h3>Dappled Fern</h3>
      <p>Pamper yourself with soft lashes, gentle facials and calm care in our cozy studio.</p>
      <div class="social"><span></span><span></span><span></span><span></span><span></span><span></span></div>
    </div>
    <div class="footer-col">
      <h3>When we work</h3>
      <p>We are open six days a week for you.<br>Mon – Fri: 9am – 7pm<br>Saturday: 10am – 4pm<br>Sunday: Closed</p>
    </div>
    <div class="footer-col">
      <h3>Contact</h3>
      <p>Call or write to book, ask a question or plan a visit.<br><br>(555) 014-2876<br>hello@dappled-fern.com</p>
    </div>
  </div>
  <div class="footer-bar">
    <ul><li>Home</li><li>About us</li><li>Services</li><li>Pricing</li><li>Book Appointment</li><li>Gallery</li><li>Contact</li></ul>
    <span>Copyright © 2015 dappled-fern.com. All Rights Reserved</span>
  </div>
</footer>

</body>
</html>
```